Pinecrest Real Estate A5 Flyer

A5 Flyer for print distribution.

Front (include attached photo and branding):
Pinecrest are a new face in the Shelley & Rossmoyne real estate market. The Pinecrest team are both Shelley ‘locals’ and are genuinely and sincerely committed to this community. They put people first and pursue exceptional outcomes for their clients. This is the founding vision of Pinecrest.

Values:
Outstanding Customer Service
Timely Communication
Integrity Always
People First
Exceptional Negotiation

If you’re thinking of selling, interested in a free market appraisal, or simply want to find out more about the Pinecrest team, please reach out to Doug or Rowan for a chat. We’d love to shout you a coffee at The Lantern Coffee + Kitchen.

Pinecrest Real Estate
E: hello@pinecrestrealestate-example.com.au
W: pinecrestrealestate-example.com.au

Back (half the page about Doug, other half the page about Rowan). Please include headshots (Rowan is the younger one):

Rowan Ferrabee (Property Consultant):

Rowan has an in-depth understanding of all things property & finance related. With a degree in property & finance, diploma in finance & mortgage broking, certificate IV in real estate practice, project management roles in residential property development, plus years of small business experience as co-founder/co-owner of The Lantern Coffee + Kitchen, his experience in managing competing demands and complex scenarios runs far and wide.

Rowan also has experience in corporate negotiations which is proving to be a very beneficial skill set. Rowan is deeply committed to people and pursuing exceptional outcomes for his clients. He has built a reputation as a man of his word who is genuine and sincere and willing to go above and beyond for his clients.

rowan@pinecrestrealestate-example.com.au
0412 306 248

Doug Penberthy (Director / Licensee):

Doug has worked in various roles inclusive of being a Real Estate Agent, Bank Manager, Financial Counsellor, Mortgage Broker, and previously a Commercial Pilot. He spent eight years in remote Western Australia, where he worked for an international mining company creating strategies to help support the well-being of employees. Doug’s focus in life has always been to help people. To him, it is always about the relationship. Doug gets enormous satisfaction from seeing individuals, families, and businesses thrive financially. He has become a skilled negotiator with extensive experience working for a number of corporations and private firms.
 
What differentiates Doug is his compassion and commitment to people. He works hard to be an excellent communicator with the aim of achieving great results. He  has extensive sales experience with incredible ability to push the boundaries, think outside the box and meet or surpass expectations. This is why his clients keep coming back and continue to refer well into the future. 

doug@pinecrestrealestate-example.com.au
0438 192 607

Target Market(s)

House Sellers / House Buyers

Industry/Entity Type

Real Estate

Colors
0054AA
0677BA
7BADD7
CADEEF
E8F1F8

Requirements
Must have
• Branding / logo, river photo, head shots, company details etc
Nice to have
• Design as per attached branding guide

```html
<!DOCTYPE html>
<html lang="en">
<head>
<meta charset="utf-8">
<title>Pinecrest Real Estate – A5 Flyer</title>
<link rel="stylesheet" href="https://fonts.googleapis.com/css2?family=Montserrat:wght@400;500;600;700&display=swap">
<style>
  :root {
    --navy: #17232e;
    --ink: #17232e;
    --white: #ffffff;
    --backdrop: #c4c4c4;
    --sky-frame: #cadeef;
    --river-deep: #1f4f86;
    --foliage: #3f5a3a;
  }
  * { box-sizing: border-box; margin: 0; padding: 0; }
  html, body { width: 1200px; height: 847px; overflow: hidden; }
  body {
    background: var(--backdrop);
    font-family: "Montserrat", Arial, sans-serif;
    color: var(--ink);
    position: relative;
  }
  .page {
    position: absolute;
    top: 68px;
    width: 502px;
    height: 711px;
    overflow: hidden;
    background: var(--white);
  }
  .page--front { left: 65px; }
  .page--back { left: 633px; }
  .abs { position: absolute; }

  /* Front */
  .hero-photo {
    left: 0; top: 0; width: 502px; height: 235px;
    background: linear-gradient(160deg, #cfe0ee 0%, #8fb3d3 14%, var(--river-deep) 38%, #23507e 62%, var(--foliage) 100%);
  }
  .front-band { left: 0; top: 239px; width: 502px; height: 310px; background: var(--navy); }
  .front-footer { left: 0; top: 645px; width: 502px; height: 66px; background: var(--navy); }

  .brand { display: flex; align-items: center; }
  .brand-mark { border-radius: 50%; flex: none; }
  .brand-name {
    font-weight: 500;
    letter-spacing: 0.32em;
    text-transform: uppercase;
  }
  .brand--front { left: 0; width: 502px; top: 259px; justify-content: center; gap: 14px; }
  .brand--front .brand-mark { width: 46px; height: 46px; background: #dfe6ea; }
  .brand--front .brand-name { font-size: 25px; color: var(--white); }

  .intro {
    left: 44px; top: 326px; width: 414px;
    color: var(--white); font-size: 10.6px; line-height: 12.9px; text-align: center;
  }
  .values-heading {
    left: 45px; top: 404px; color: var(--white);
    font-size: 14px; font-weight: 600; display: flex; align-items: center; gap: 7px;
  }
  .values-heading::after { content: ""; width: 125px; height: 1px; background: var(--white); }
  .values-list {
    left: 45px; top: 432px; list-style: none; color: var(--white);
    font-size: 11px; font-weight: 500;
  }
  .values-list li { height: 20.4px; display: flex; align-items: center; gap: 8px; }
  .values-list li::before { content: ""; width: 4px; height: 4px; border-radius: 50%; background: var(--white); }

  .river-photo {
    left: 286px; top: 405px; width: 171px; height: 225px;
    border: 5px solid var(--sky-frame);
    background: linear-gradient(180deg, #eef3f7 0%, #c9d8e4 20%, #5a7c9a 38%, var(--river-deep) 60%, #17375f 100%);
  }
  .invite {
    left: 44px; top: 568px; width: 228px;
    font-size: 8.6px; line-height: 10.8px; color: var(--ink);
  }

  .contact-line {
    display: flex; align-items: center; gap: 7px; white-space: nowrap;
  }
  .contact-line svg { flex: none; }
  .footer-line { font-size: 8px; top: 672px; }
  .footer-email { left: 20px; }
  .footer-web { right: 20px; }
  .page--front .footer-line { color: var(--white); }
  .page--back .footer-line { color: var(--ink); }

  /* Back */
  .back-band { left: 0; top: 314px; width: 502px; height: 331px; background: var(--navy); }
  .brand--back { left: 247px; top: 21px; gap: 10px; }
  .brand--back .brand-mark { width: 38px; height: 38px; background: var(--navy); }
  .brand--back .brand-name { font-size: 20px; color: var(--ink); }

  .person-name { position: absolute; left: 22px; font-size: 15px; font-weight: 700; }
  .person-role { position: absolute; left: 22px; font-size: 12px; font-weight: 600; }
  .bio {
    position: absolute; left: 22px;
    width: 283px; font-size: 8.6px; line-height: 10.75px; text-align: justify;
  }
  .bio p + p { margin-top: 10.75px; }
  .person-contact { position: absolute; left: 22px; font-size: 10.5px; font-weight: 500; }

  .headshot { position: absolute; left: 322px; width: 158px; height: 196px; border: 5px solid var(--navy); }
  .headshot--rowan { top: 86px; background: linear-gradient(180deg, #dcdcdc 0%, #cfcfcf 55%, #2c3d5c 100%); }
  .headshot--doug { top: 379px; border-color: var(--white); background: linear-gradient(180deg, #efefef 0%, #e2e2e2 55%, #2b4470 100%); }

  .section-rowan { color: var(--ink); }
  .section-rowan .person-name { top: 48px; }
  .section-rowan .person-role { top: 67px; }
  .section-rowan .bio { top: 91px; }
  .section-rowan .contact-email { top: 264px; }
  .section-rowan .contact-phone { top: 284px; }

  .section-doug { color: var(--white); }
  .section-doug .person-name { top: 329px; }
  .section-doug .person-role { top: 347px; }
  .section-doug .bio { top: 376px; }
  .section-doug .contact-email { top: 590px; }
  .section-doug .contact-phone { top: 610px; }
</style>
</head>
<body>

<section class="page page--front">
  <div class="abs hero-photo" role="img" aria-label="Aerial photo of the river foreshore with homes, trees and the city skyline"></div>
  <div class="abs front-band"></div>

  <div class="abs brand brand--front">
    <span class="brand-mark"></span>
    <span class="brand-name">Pinecrest</span>
  </div>

  <p class="abs intro">Pinecrest are a new face in the Shelley &amp; Rossmoyne real estate market. The Pinecrest team are both Shelley ‘locals’ and are genuinely and sincerely committed to this community. They put people first and pursue exceptional outcomes for their clients. This is the founding vision of Pinecrest.</p>

  <h2 class="abs values-heading">Values:</h2>
  <ul class="abs values-list">
    <li>Outstanding Customer Service</li>
    <li>Timely Communication</li>
    <li>Integrity Always</li>
    <li>People First</li>
    <li>Exceptional Negotiation</li>
  </ul>

  <div class="abs river-photo" role="img" aria-label="Aerial photo of the river with apartment towers and moored boats"></div>

  <p class="abs invite">If you’re thinking of selling, interested in a free market appraisal, or simply want to find out more about the Pinecrest team, please reach out to Doug or Rowan for a chat. We’d love to shout you a coffee at The Lantern Coffee + Kitchen.</p>

  <div class="abs front-footer"></div>
  <div class="abs contact-line footer-line footer-email">
    <svg width="15" height="11" viewBox="0 0 16 12"><rect x="0.5" y="0.5" width="15" height="11" rx="1" fill="currentColor"/><path d="M1 1.5 8 7l7-5.5" fill="none" stroke="#17232e" stroke-width="1.2"/></svg>
    <span>hello@pinecrestrealestate-example.com.au</span>
  </div>
  <div class="abs contact-line footer-line footer-web">
    <svg width="13" height="13" viewBox="0 0 14 14" fill="none" stroke="currentColor" stroke-width="1.1"><circle cx="7" cy="7" r="6.2"/><ellipse cx="7" cy="7" rx="2.8" ry="6.2"/><path d="M0.8 7h12.4M2 3.6h10M2 10.4h10"/></svg>
    <span>www.pinecrestrealestate-example.com.au</span>
  </div>
</section>

<section class="page page--back">
  <div class="abs back-band"></div>

  <div class="abs brand brand--back">
    <span class="brand-mark"></span>
    <span class="brand-name">Pinecrest</span>
  </div>

  <div class="section-rowan">
    <h2 class="person-name">Rowan Ferrabee</h2>
    <p class="person-role">Property Consultant</p>
    <div class="bio">
      <p>Rowan has an in-depth understanding of all things property &amp; finance related. With a degree in property &amp; finance, diploma in finance &amp; mortgage broking, certificate IV in real estate practice, project management roles in residential property development, plus years of small business experience as co-founder/co-owner of The Lantern Coffee + Kitchen, his experience in managing competing demands and complex scenarios runs far and wide.</p>
      <p>Rowan also has experience in corporate negotiations which is proving to be a very beneficial skill set. Rowan is deeply committed to people and pursuing exceptional outcomes for his clients. He has built a reputation as a man of his word who is genuine and sincere and willing to go above and beyond for his clients.</p>
    </div>
    <div class="contact-line person-contact contact-email">
      <svg width="16" height="12" viewBox="0 0 16 12"><rect x="0.5" y="0.5" width="15" height="11" rx="1" fill="currentColor"/><path d="M1 1.5 8 7l7-5.5" fill="none" stroke="#fff" stroke-width="1.2"/></svg>
      <span>rowan@pinecrestrealestate-example.com.au</span>
    </div>
    <div class="contact-line person-contact contact-phone">
      <svg width="16" height="15" viewBox="0 0 16 15"><path d="M3.2 1.2 5.4 4 4 5.6c.9 1.9 2.4 3.4 4.3 4.3l1.6-1.4 2.8 2.2-1.3 2.2C6.6 12.6 2.3 8.4 1.1 3.5Z" fill="currentColor"/><path d="M9.5 1.5a4.5 4.5 0 0 1 4 4M9.3 3.6a2.4 2.4 0 0 1 2.1 2.1" fill="none" stroke="currentColor" stroke-width="1.1"/></svg>
      <span>0412 306 248</span>
    </div>
  </div>
  <div class="headshot headshot--rowan" role="img" aria-label="Headshot of Rowan Ferrabee in a navy suit"></div>

  <div class="section-doug">
    <h2 class="person-name">Doug Penberthy</h2>
    <p class="person-role">Director / Licensee</p>
    <div class="bio">
      <p>Doug has worked in various roles inclusive of being a Real Estate Agent, Bank Manager, Financial Counsellor, Mortgage Broker, and previously a Commercial Pilot. He spent eight years in remote Western Australia, where he worked for an international mining company creating strategies to help support the well-being of employees. Doug’s focus in life has always been to help people. To him, it is always about the relationship. Doug gets enormous satisfaction from seeing individuals, families, and businesses thrive financially. He has become a skilled negotiator with extensive experience working for a number of corporations and private firms.</p>
      <p>What differentiates Doug is his compassion and commitment to people. He works hard to be an excellent communicator with the aim of achieving great results. He has extensive sales experience with incredible ability to push the boundaries, think outside the box and meet or surpass expectations. This is why his clients keep coming back and continue to refer well into the future.</p>
    </div>
    <div class="contact-line person-contact contact-email">
      <svg width="16" height="12" viewBox="0 0 16 12"><rect x="0.5" y="0.5" width="15" height="11" rx="1" fill="currentColor"/><path d="M1 1.5 8 7l7-5.5" fill="none" stroke="#17232e" stroke-width="1.2"/></svg>
      <span>doug@pinecrestrealestate-example.com.au</span>
    </div>
    <div class="contact-line person-contact contact-phone">
      <svg width="16" height="15" viewBox="0 0 16 15"><path d="M3.2 1.2 5.4 4 4 5.6c.9 1.9 2.4 3.4 4.3 4.3l1.6-1.4 2.8 2.2-1.3 2.2C6.6 12.6 2.3 8.4 1.1 3.5Z" fill="currentColor"/><path d="M9.5 1.5a4.5 4.5 0 0 1 4 4M9.3 3.6a2.4 2.4 0 0 1 2.1 2.1" fill="none" stroke="currentColor" stroke-width="1.1"/></svg>
      <span>0438 192 607</span>
    </div>
  </div>
  <div class="headshot headshot--doug" role="img" aria-label="Headshot of Doug Penberthy in a navy suit and striped tie"></div>

  <div class="abs contact-line footer-line footer-email">
    <svg width="15" height="11" viewBox="0 0 16 12"><rect x="0.5" y="0.5" width="15" height="11" rx="1" fill="currentColor"/><path d="M1 1.5 8 7l7-5.5" fill="none" stroke="#fff" stroke-width="1.2"/></svg>
    <span>hello@pinecrestrealestate-example.com.au</span>
  </div>
  <div class="abs contact-line footer-line footer-web">
    <svg width="13" height="13" viewBox="0 0 14 14" fill="none" stroke="currentColor" stroke-width="1.1"><circle cx="7" cy="7" r="6.2"/><ellipse cx="7" cy="7" rx="2.8" ry="6.2"/><path d="M0.8 7h12.4M2 3.6h10M2 10.4h10"/></svg>
    <span>www.pinecrestrealestate-example.com.au</span>
  </div>
</section>

</body>
</html>
```